Zelvo - revolutionary mobile payment

The app is a P2P money trasfert, without the using of credit card or bank circuits it can transfer electronic money from one person to another consumers simply and immediatelly.
You can use the color you want, but the message we need to transert to consumer is simplicity, safety and coolness.
In attach the logo of the company and the wireframe of thre page of the app.
The goal is to design the page of the app with a clear, simple and intuitive graphic.
Updates

I have upgrade the brief with important information and detail, many thanks

Target Market(s)

all the people

Industry/Entity Type

Credit Card

Requirements
Must have
• You have to design one icon for each button in the first page, (shop is: where to shop)
in the second one a new intuitive image (instead of the hand) that let the user to understand that with a simple swipe he can process the payment
Nice to have
• You can include or esxclude what you want or belive can improve user experience of the app
Should not have
• too much color, too much button or information

```html
<!DOCTYPE html>
<html lang="en">
<head>
<meta charset="utf-8">
<title>Zelvo – Home</title>
<link rel="stylesheet" href="https://fonts.googleapis.com/css2?family=Roboto:wght@400;500;700;900&display=swap">
<style>
  :root {
    --ink-black: #0b0b0c;
    --status-text: #f2f2f2;
    --header-white: #ffffff;
    --brand-navy: #1c3d7a;
    --number-bar: rgba(40, 40, 42, 0.78);
    --plan-blue-top: #3f6fb8;
    --plan-blue-bottom: #1f4890;
    --tile-blue-top: #2c6fcf;
    --tile-blue-bottom: #0f4597;
    --tile-grey: rgba(96, 96, 98, 0.72);
    --tile-grey-edge: rgba(180, 180, 182, 0.35);
    --icon-grey: #c9c9cb;
    --label-white: #ffffff;
    --bg-warm-1: #a79d91;
    --bg-warm-2: #d8cfc3;
    --bg-warm-3: #7d7670;
  }
  * { box-sizing: border-box; margin: 0; padding: 0; }
  html, body {
    width: 1200px; height: 2240px; overflow: hidden;
    background: var(--ink-black);
    font-family: "Roboto", Arial, sans-serif;
  }
  .app-screen {
    position: relative; width: 1200px; height: 2240px; overflow: hidden;
  }
  .backdrop-photo {
    position: absolute; left: 0; top: 340px; width: 1200px; height: 1900px;
    background:
      radial-gradient(ellipse 520px 700px at 40% 30%, var(--bg-warm-2), transparent 70%),
      radial-gradient(ellipse 600px 800px at 85% 60%, #b8b2ab, transparent 70%),
      linear-gradient(180deg, var(--bg-warm-1) 0%, #9c958d 50%, var(--bg-warm-3) 100%);
  }
  .status-bar {
    position: absolute; left: 0; top: 0; width: 1200px; height: 90px;
    background: var(--ink-black); color: var(--status-text);
    display: flex; align-items: center; justify-content: space-between;
    padding: 0 30px; font-size: 40px; font-weight: 500;
  }
  .status-left { display: flex; align-items: center; gap: 14px; }
  .status-time { position: absolute; left: 0; right: 0; text-align: center; pointer-events: none; }
  .status-right { display: flex; align-items: center; gap: 14px; }
  .brand-header {
    position: absolute; left: 0; top: 90px; width: 1200px; height: 250px;
    background: var(--header-white);
    display: flex; align-items: center; justify-content: center; gap: 26px;
  }
  .brand-dot {
    width: 120px; height: 120px; border-radius: 50%; background: var(--brand-navy);
  }
  .brand-name {
    font-size: 130px; font-weight: 900; color: var(--brand-navy); letter-spacing: 2px;
  }
  .number-bar {
    position: absolute; left: 0; top: 340px; width: 1200px; height: 130px;
    background: var(--number-bar);
    display: flex; align-items: center; justify-content: space-between;
    padding: 0 50px; color: var(--label-white); font-size: 52px; font-weight: 400;
  }
  .plan-bar {
    position: absolute; left: 0; top: 470px; width: 1200px; height: 175px;
    background: linear-gradient(180deg, var(--plan-blue-top), var(--plan-blue-bottom));
    display: flex; align-items: center; padding: 0 40px; gap: 34px;
    border-top: 3px solid rgba(255,255,255,0.25);
  }
  .plan-avatar {
    width: 136px; height: 136px; border-radius: 50%;
    border: 6px solid #ffffff;
    background: radial-gradient(circle at 50% 40%, #d9b39a, #7a4a3a);
  }
  .plan-name {
    flex: 1; color: var(--label-white); font-size: 110px; font-weight: 400; letter-spacing: 2px;
  }
  .menu-icon { width: 84px; height: 70px; }
  .action-grid {
    position: absolute; left: 50px; top: 710px; width: 1100px;
    display: grid; grid-template-columns: 510px 510px; grid-auto-rows: 590px;
    column-gap: 80px; row-gap: 70px;
  }
  .action-tile {
    position: relative; overflow: hidden;
    background: var(--tile-grey);
    border: 2px solid var(--tile-grey-edge);
    display: flex; flex-direction: column; align-items: center; justify-content: center;
  }
  .action-tile::after {
    content: ""; position: absolute; right: 0; top: 0; width: 200px; height: 200px;
    background: linear-gradient(225deg, rgba(255,255,255,0.28) 50%, transparent 50%);
  }
  .action-tile--primary {
    background: linear-gradient(180deg, var(--tile-blue-top), var(--tile-blue-bottom));
    border-color: rgba(255,255,255,0.3);
  }
  .action-icon { width: 300px; height: 260px; margin-top: -20px; }
  .action-label {
    position: absolute; bottom: 38px; left: 0; right: 0; text-align: center;
    color: var(--label-white); font-size: 52px; font-weight: 500; letter-spacing: 1px;
  }
</style>
</head>
<body>
<main class="app-screen">
  <div class="backdrop-photo" role="img" aria-label="Softly blurred photo of a person in a bright office"></div>

  <header class="status-bar">
    <div class="status-left">
      <svg width="70" height="34" viewBox="0 0 70 34" aria-hidden="true">
        <rect x="0" y="24" width="10" height="10" fill="#f2f2f2"/>
        <rect x="14" y="18" width="10" height="16" fill="#f2f2f2"/>
        <rect x="28" y="12" width="10" height="22" fill="#f2f2f2"/>
        <rect x="42" y="6" width="10" height="28" fill="#f2f2f2"/>
        <rect x="56" y="0" width="10" height="34" fill="#f2f2f2"/>
      </svg>
      <span>Nettel</span>
    </div>
    <span class="status-time">8:33 PM</span>
    <div class="status-right">
      <svg width="40" height="40" viewBox="0 0 40 40" aria-hidden="true"><circle cx="20" cy="20" r="16" fill="none" stroke="#f2f2f2" stroke-width="4"/><path d="M20 8 L20 20 L28 24" stroke="#f2f2f2" stroke-width="4" fill="none"/></svg>
      <svg width="36" height="40" viewBox="0 0 36 40" aria-hidden="true"><path d="M34 2 L2 18 L18 20 L20 38 Z" fill="#f2f2f2"/></svg>
      <svg width="96" height="40" viewBox="0 0 96 40" aria-hidden="true"><rect x="2" y="4" width="84" height="32" rx="6" fill="none" stroke="#f2f2f2" stroke-width="3"/><rect x="7" y="9" width="74" height="22" rx="3" fill="#f2f2f2"/><rect x="88" y="13" width="6" height="14" rx="2" fill="#f2f2f2"/></svg>
    </div>
  </header>

  <section class="brand-header">
    <span class="brand-dot"></span>
    <span class="brand-name">Zelvo</span>
  </section>

  <section class="number-bar">
    <span class="account-number">+395550142</span>
    <svg class="settings-icon" width="76" height="76" viewBox="0 0 76 76" aria-label="Settings">
      <g fill="#ffffff" transform="translate(38 38)">
        <rect x="-7" y="-36" width="14" height="16" rx="2"/>
        <rect x="-7" y="-36" width="14" height="16" rx="2" transform="rotate(45)"/>
        <rect x="-7" y="-36" width="14" height="16" rx="2" transform="rotate(90)"/>
        <rect x="-7" y="-36" width="14" height="16" rx="2" transform="rotate(135)"/>
        <rect x="-7" y="-36" width="14" height="16" rx="2" transform="rotate(180)"/>
        <rect x="-7" y="-36" width="14" height="16" rx="2" transform="rotate(225)"/>
        <rect x="-7" y="-36" width="14" height="16" rx="2" transform="rotate(270)"/>
        <rect x="-7" y="-36" width="14" height="16" rx="2" transform="rotate(315)"/>
        <circle r="24"/>
      </g>
      <circle cx="38" cy="38" r="10" fill="#3a3a3c"/>
    </svg>
  </section>

  <section class="plan-bar">
    <div class="plan-avatar" role="img" aria-label="User profile photo"></div>
    <span class="plan-name">BASIC</span>
    <svg class="menu-icon" viewBox="0 0 84 70" aria-label="Menu">
      <rect x="0" y="2" width="84" height="14" rx="3" fill="#ffffff"/>
      <rect x="0" y="28" width="84" height="14" rx="3" fill="#ffffff"/>
      <rect x="0" y="54" width="84" height="14" rx="3" fill="#ffffff"/>
    </svg>
  </section>

  <nav class="action-grid">
    <a class="action-tile action-tile--primary">
      <svg class="action-icon" viewBox="0 0 300 260" aria-hidden="true">
        <rect x="10" y="50" width="230" height="160" rx="14" fill="none" stroke="#ffffff" stroke-width="12"/>
        <rect x="10" y="88" width="230" height="26" fill="#ffffff"/>
        <rect x="36" y="150" width="90" height="14" fill="#ffffff"/>
        <rect x="36" y="174" width="60" height="14" fill="#ffffff"/>
        <text x="225" y="220" text-anchor="middle" font-family="Roboto, Arial, sans-serif" font-size="220" font-weight="900" fill="#ffffff" stroke="#1a56b0" stroke-width="10" paint-order="stroke">$</text>
      </svg>
      <span class="action-label">PAY</span>
    </a>
    <a class="action-tile">
      <svg class="action-icon" viewBox="0 0 300 260" aria-hidden="true">
        <path d="M70 140 V110 a80 80 0 0 1 160 0 V140" fill="none" stroke="var(--icon-grey)" stroke-width="16"/>
        <rect x="46" y="126" width="44" height="80" rx="16" fill="var(--icon-grey)"/>
        <rect x="210" y="126" width="44" height="80" rx="16" fill="var(--icon-grey)"/>
        <path d="M232 204 q0 40 -60 44" fill="none" stroke="var(--icon-grey)" stroke-width="10"/>
        <rect x="148" y="236" width="32" height="18" rx="8" fill="var(--icon-grey)"/>
        <text x="150" y="200" text-anchor="middle" font-family="Roboto, Arial, sans-serif" font-size="120" font-weight="900" fill="var(--icon-grey)">?</text>
      </svg>
      <span class="action-label">ASK</span>
    </a>
    <a class="action-tile">
      <svg class="action-icon" viewBox="0 0 300 260" aria-hidden="true">
        <rect x="30" y="40" width="240" height="170" rx="12" fill="none" stroke="var(--icon-grey)" stroke-width="12"/>
        <rect x="110" y="22" width="80" height="30" rx="6" fill="var(--icon-grey)"/>
        <circle cx="95" cy="110" r="24" fill="var(--icon-grey)"/>
        <path d="M55 180 q0 -42 40 -42 q40 0 40 42 Z" fill="var(--icon-grey)"/>
        <rect x="150" y="96" width="44" height="14" fill="var(--icon-grey)"/>
        <rect x="150" y="124" width="44" height="14" fill="var(--icon-grey)"/>
        <rect x="150" y="152" width="44" height="14" fill="var(--icon-grey)"/>
        <text x="230" y="168" text-anchor="middle" font-family="Roboto, Arial, sans-serif" font-size="100" font-weight="900" fill="var(--icon-grey)">$</text>
      </svg>
      <span class="action-label">ACCOUNT</span>
    </a>
    <a class="action-tile">
      <svg class="action-icon" viewBox="0 0 300 260" aria-hidden="true">
        <path d="M115 90 V66 a35 35 0 0 1 70 0 V90" fill="none" stroke="var(--icon-grey)" stroke-width="12"/>
        <path d="M82 80 H218 L236 236 H64 Z" fill="var(--icon-grey)"/>
      </svg>
      <span class="action-label">SHOP</span>
    </a>
  </nav>
</main>
</body>
</html>
```